Attorney Recruiting company needs brochure

Brief Harbor is a company that recruits attorneys for law firms and corporations. We want a brochure that makes the law firms and corporation want to retain us to recruit attorneys when they are hiring. We identify experienced well qualified attorneys. We provide them for direct hire (also knows as permanent placement) and for temporary contract hourly work. We want our colors included: red, black and white. It has to convey professionalism and experience. You can find lots of information about who we are and what we do on our website. www.briefharbor-example.com. The brochure should be in traditional conservative font. Should be easy to read. Attorneys tend to scan brochures to see what we do, they will need read it word for word, so we don't need lots of paragraphs and extraneous text. The brochure should outline easily the services we provide which are very specific. They are outlined on home page of website. You should also include our logo which I will attach in several formats.

Target Market(s)

Attorneys and executives

Industry/Entity Type

Conservative

Requirements
Must have
• logo
colors described above

```html
<!DOCTYPE html>
<html lang="en">
<head>
<meta charset="utf-8">
<title>Brief Harbor — How We Recruit Attorneys for Employers</title>
<link rel="stylesheet" href="https://fonts.googleapis.com/css2?family=Arimo:ital,wght@0,700;1,400&family=Black+Ops+One&display=swap">
<style>
  :root {
    --brand-red: #a41d21;
    --brand-red-deep: #8f171b;
    --paper: #ffffff;
    --slate: #6b6d70;
    --photo-dark: #3a2f2b;
    --photo-mid: #7a6a5e;
    --photo-light: #c9bcae;
  }
  * { margin: 0; padding: 0; box-sizing: border-box; }
  html, body {
    width: 1200px;
    height: 848px;
    overflow: hidden;
    background: var(--brand-red);
  }
  .page {
    position: relative;
    width: 1200px;
    height: 848px;
    background: var(--brand-red);
    font-family: "Arimo", Arial, sans-serif;
  }
  .accent-tab {
    position: absolute;
    left: 0; top: 17px;
    width: 311px; height: 43px;
    background: var(--brand-red-deep);
  }
  .title-banner {
    position: absolute;
    left: 0; top: 60px;
    width: 798px; height: 94px;
    background: var(--paper);
    display: flex;
    align-items: center;
    padding-left: 53px;
  }
  .title-banner h1 {
    color: var(--brand-red);
    font-family: "Arimo", Arial, sans-serif;
    font-weight: 700;
    font-size: 28px;
    letter-spacing: 0.2px;
  }
  .courtroom-photo {
    position: absolute;
    left: 0; top: 154px;
    width: 299px; height: 590px;
    background: linear-gradient(160deg, var(--photo-light) 0%, var(--photo-mid) 40%, var(--photo-dark) 100%);
  }
  .photo-footer {
    position: absolute;
    left: 0; top: 744px;
    width: 299px; height: 104px;
    background: var(--slate);
  }
  .process {
    position: absolute;
    left: 335px; top: 218px;
    width: 822px;
    color: var(--paper);
  }
  .step { margin-bottom: 30px; }
  .step h2 {
    font-family: "Black Ops One", "Arial Black", sans-serif;
    font-weight: 400;
    font-size: 17px;
    letter-spacing: 1px;
    margin-bottom: 12px;
  }
  .step p {
    font-style: italic;
    font-size: 12.4px;
    line-height: 19px;
    text-transform: uppercase;
  }
</style>
</head>
<body>
<main class="page">
  <div class="accent-tab"></div>
  <header class="title-banner">
    <h1>HOW WE RECRUIT ATTORNEYS FOR EMPLOYERS</h1>
  </header>

  <div class="courtroom-photo" role="img" aria-label="Photograph of attorneys standing before a judge at the bench in a courtroom"></div>
  <div class="photo-footer"></div>

  <section class="process">
    <article class="step">
      <h2>1. MEET THE EMPLOYER</h2>
      <p>We want to meet with you personally whenever possible to ensure we understand exactly what you need. We want to appreciate both the tangible and intangible aspects of the position. Visiting the office and meeting the people with whom the attorney will work is generally very helpful but not required.</p>
    </article>
    <article class="step">
      <h2>2. RECRUIT ATTORNEYS</h2>
      <p>We are very well networked in the legal community and have reliable referral sources in every area of law and business. We also have an established database of attorneys who are either active or passive job seekers that have confidentially requested us to let them know when the “right position” is available. When needed we also conduct general and targeted advertising.</p>
    </article>
    <article class="step">
      <h2>3. SCREEN ATTORNEYS</h2>
      <p>We interview potential candidates with our proven interview system. We conduct reference checks, except where employer prefers to complete reference checks. We confirm that state bar membership is in good standing where applicable.</p>
    </article>
    <article class="step">
      <h2>4. FACILITATE INTERVIEW AND HIRING</h2>
      <p>We will present you with resumes and significant commentary from our screening process for the top candidates. You may only need to meet two or three attorney candidates unless you prefer to consider more. We are available to be involved in any aspect of salary and benefit negotiations.</p>
    </article>
  </section>
</main>
</body>
</html>
```